Men's enhance supplement package design (square form)

WHAT WE WANT TO TELL BY DESIGN:Male enhancement, enhance Sexual vitality, strong man, get (back) desire forsex, masculinity, booster.This supplement is not like Dunelto but want to tell like Dunelto by design.
Target Market(s)
Online. age over 20 men

```html
<!DOCTYPE html>
<html lang="en">
<head>
<meta charset="utf-8">
<title>Vyrexon – Original Formula for Man</title>
<link rel="stylesheet" href="https://fonts.googleapis.com/css2?family=Audiowide&family=Black+Ops+One&family=Open+Sans:wght@400;600&display=swap">
<style>
  :root {
    --bg: #f4f4f4;
    --pouch: #0d0d0d;
    --pouch-edge: #1c1c1c;
    --label-bg: #161616;
    --label-border: #5a5a5a;
    --gold-1: #f6c443;
    --gold-2: #e07a1c;
    --gold-3: #b5361a;
    --silver: #d9d9d9;
    --ink-dark: #1d1d1d;
    --text-light: #f1f1f1;
    --red: #d8242c;
  }
  * { margin: 0; padding: 0; box-sizing: border-box; }
  html, body { width: 865px; height: 1200px; overflow: hidden; background: var(--bg); }
  .canvas { position: relative; width: 865px; height: 1200px; }

  .pouch {
    position: absolute; left: 80px; top: 33px; width: 704px; height: 1134px;
    background: linear-gradient(180deg, var(--pouch-edge), var(--pouch) 30%, var(--pouch));
    border-radius: 6px;
  }
  .pouch .zip-line {
    position: absolute; left: 0; right: 0; height: 3px; background: #262626;
  }
  .zip-line.top { top: 118px; }
  .zip-line.bottom { top: 140px; }

  .label {
    position: absolute; left: 95px; top: 304px; width: 520px; height: 730px;
    background: radial-gradient(circle at 50% 45%, #262626, var(--label-bg) 70%);
    border: 6px solid var(--label-border);
    border-radius: 26px;
    overflow: hidden;
  }
  .brand {
    position: absolute; left: 0; right: 0; top: 62px;
    text-align: center;
    font-family: "Audiowide", sans-serif; font-size: 78px; letter-spacing: 2px;
    background: linear-gradient(90deg, var(--gold-2), var(--gold-1) 45%, var(--gold-1) 60%, var(--gold-3));
    -webkit-background-clip: text; background-clip: text; color: transparent;
    line-height: 1;
  }
  .hero {
    position: absolute; left: 37px; top: 163px; width: 378px; height: 331px;
    background: radial-gradient(ellipse at 55% 45%, #5a3a28 0%, #3a2216 40%, #c24a14 75%, rgba(20,20,20,0) 100%);
    border-radius: 40% 40% 30% 30%;
  }
  .swirl {
    position: absolute; border-radius: 50%;
    background: radial-gradient(circle, rgba(190,130,50,0.55), rgba(120,60,20,0.25) 60%, rgba(0,0,0,0) 72%);
  }
  .swirl.right-top { left: 372px; top: 185px; width: 110px; height: 110px; }
  .swirl.left-mid { left: 20px; top: 290px; width: 150px; height: 190px; }
  .swirl.right-low { left: 345px; top: 500px; width: 140px; height: 110px; }

  .tagline {
    position: absolute; left: 52px; top: 509px; width: 436px; height: 27px;
    background: linear-gradient(90deg, #9b9b9b, var(--silver) 40%, #ffffff 70%, #a8a8a8);
    transform: skewX(-12deg);
    display: flex; align-items: center; justify-content: center;
  }
  .tagline span {
    transform: skewX(12deg);
    font-family: "Black Ops One", sans-serif; font-size: 19px; letter-spacing: 1.5px;
    color: var(--ink-dark);
  }
  .ingredients {
    position: absolute; left: 50px; top: 578px; width: 275px;
    text-align: center;
    font-family: "Open Sans", sans-serif; font-size: 11.5px; line-height: 15.5px;
    color: var(--text-light); text-transform: uppercase; letter-spacing: -0.2px;
  }
  .category {
    position: absolute; left: 58px; top: 660px;
    font-family: "Black Ops One", sans-serif; font-size: 18px; letter-spacing: 0.5px;
    color: var(--red);
  }
  .count-badge {
    position: absolute; left: 357px; top: 588px; width: 81px; height: 89px;
    border: 4px solid #bdbdbd; border-radius: 40px 40px 4px 4px;
    background: #101010;
    text-align: center; color: #ffffff;
  }
  .count-badge .qty {
    display: block; margin-top: 12px;
    font-family: "Audiowide", sans-serif; font-size: 36px; line-height: 1;
  }
  .count-badge .unit {
    display: block; margin-top: 12px;
    font-family: "Black Ops One", sans-serif; font-size: 10px; letter-spacing: 0.5px;
  }
</style>
</head>
<body>
<div class="canvas">
  <div class="pouch">
    <div class="zip-line top"></div>
    <div class="zip-line bottom"></div>

    <section class="label">
      <div class="swirl right-top" role="img" aria-label="Gold circular swirl decoration"></div>
      <div class="swirl left-mid" role="img" aria-label="Gold circular swirl decoration"></div>
      <div class="swirl right-low" role="img" aria-label="Gold circular swirl decoration"></div>

      <h1 class="brand">VYREXON</h1>

      <div class="hero" role="img" aria-label="Muscular male torso surrounded by flames"></div>

      <div class="tagline"><span>ORIGINAL FORMULA FOR MAN</span></div>

      <p class="ingredients">
        Maca, Zinc, Iron, Kra Chai Dahm,<br>
        Cistanche Tubulosa, Soft-Shelled Turtle,<br>
        L-Arginin, L-Citrulline, L-Leucine, L-Valine,<br>
        L-Isoleucine
      </p>

      <p class="category">DIETARY SUPPLEMENT</p>

      <div class="count-badge">
        <span class="qty">90</span>
        <span class="unit">TABLETS</span>
      </div>
    </section>
  </div>
</div>
</body>
</html>
```